Marlowe Tots Wipes Packaging

Brand: Marlowe Tots
Packaging needed: Baby Wipes

Create a new brand for baby wipes called Marlowe Tots. This logo can include character/icons geared towards the baby/parent market.

Use Tavvies/Dorlins for copy reference for now.

**Please note that we would like to see more festive cartoon options like the characters such as Tilly Thimbledown. More colorful colors and characters.*****

Target Market(s)

Parents/Mothers

Industry/Entity Type

Baby

```html
<!DOCTYPE html>
<html lang="en">
<head>
<meta charset="utf-8">
<title>Marlowe Tots Baby Wipes – Pack Label</title>
<link rel="stylesheet" href="https://fonts.googleapis.com/css2?family=Delius&family=Arimo:wght@400;700&display=swap">
<style>
  :root {
    --page: #ffffff;
    --sky: #5bbcf2;
    --sky-deep: #3fb0ee;
    --lime: #7be35a;
    --navy: #133a63;
    --pink: #f4798f;
    --pink-soft: #f7a3b4;
    --card: #f3f7f7;
    --tab: #b9c0c6;
    --white: #ffffff;
  }
  * { margin: 0; padding: 0; box-sizing: border-box; }
  html, body { width: 1200px; height: 1000px; overflow: hidden; background: var(--page); }
  body { position: relative; font-family: "Arimo", Arial, sans-serif; }

  .pack-label {
    position: absolute; left: 30px; top: 268px; width: 1137px; height: 444px;
    box-shadow: 0 3px 8px rgba(0,0,0,.45);
    overflow: hidden; background: var(--sky);
  }
  .pack-art { position: absolute; inset: 0; }

  .logo-panel {
    position: absolute; left: 368px; top: 187px; width: 492px; height: 132px;
    border-radius: 18px; background: var(--sky-deep);
    border: 5px solid rgba(255,255,255,.85);
  }
  .wordmark {
    position: absolute; left: 0; right: 0; top: 10px; text-align: center;
    font-family: "Delius", "Comic Sans MS", cursive; font-size: 62px; color: var(--white);
    letter-spacing: 1px; white-space: nowrap;
  }
  .logo-descriptor {
    position: absolute; left: 56px; top: 82px;
    font-weight: 700; font-size: 24px; color: var(--navy); letter-spacing: .5px;
  }

  .open-tab {
    position: absolute; left: 940px; top: 184px; width: 28px; height: 128px;
    background: var(--tab);
    display: flex; align-items: center; justify-content: center;
  }
  .open-tab span {
    writing-mode: vertical-rl; font-size: 15px; letter-spacing: 1.5px; color: #222;
  }

  .mini-brand { position: absolute; left: 586px; top: 374px; }
  .mini-brand .wordmark-small {
    font-family: "Delius", "Comic Sans MS", cursive; font-size: 30px; color: var(--white);
    line-height: 1; white-space: nowrap;
  }
  .mini-brand .line-a { font-weight: 700; font-size: 10px; color: var(--navy); margin-top: 5px; }
  .mini-brand .line-b { font-weight: 700; font-size: 12px; color: var(--navy); }

  .count-block { position: absolute; left: 791px; top: 386px; display: flex; gap: 8px; }
  .count-badge {
    width: 42px; height: 36px; border-radius: 7px; background: var(--pink);
    color: var(--white); font-weight: 700; font-size: 24px;
    display: flex; align-items: center; justify-content: center;
  }
  .count-text .claim { font-weight: 700; font-size: 15px; color: var(--navy); }
  .count-text .size { font-size: 11px; color: var(--navy); margin-top: 3px; }

  .fibre-claim { position: absolute; left: 1022px; top: 368px; line-height: 1; }
  .fibre-claim .with { font-size: 15px; color: var(--lime); }
  .fibre-claim .natural { font-weight: 700; font-size: 23px; color: var(--white); }
  .fibre-claim .fibres { font-size: 21px; color: var(--lime); }

  .proof-badge {
    position: absolute; left: 1008px; top: 8px; width: 124px;
    text-align: center; line-height: 1;
  }
  .proof-badge .big { font-weight: 700; font-size: 23px; color: var(--navy); white-space: nowrap; }
  .proof-badge .pill {
    display: inline-block; margin: 2px 0; padding: 2px 10px; border-radius: 9px;
    background: var(--pink-soft); font-size: 9px; color: var(--navy); white-space: nowrap;
  }
</style>
</head>
<body>
  <section class="pack-label">
    <svg class="pack-art" width="1137" height="444" viewBox="0 0 1137 444">
      <defs>
        <linearGradient id="photoTone" x1="0" y1="0" x2="1" y2="0">
          <stop offset="0" stop-color="#c98f72"/>
          <stop offset=".2" stop-color="#e7b89e"/>
          <stop offset=".5" stop-color="#f4d6c6"/>
          <stop offset=".8" stop-color="#f6ece7"/>
          <stop offset="1" stop-color="#f7f5f4"/>
        </linearGradient>
        <radialGradient id="photoGlow" cx=".55" cy=".45" r=".45">
          <stop offset="0" stop-color="#f9dccd" stop-opacity=".9"/>
          <stop offset="1" stop-color="#f9dccd" stop-opacity="0"/>
        </radialGradient>
        <linearGradient id="photoLower" x1="0" y1="0" x2="0" y2="1">
          <stop offset=".55" stop-color="#ffffff" stop-opacity="0"/>
          <stop offset="1" stop-color="#f1eeec" stop-opacity=".85"/>
        </linearGradient>
        <radialGradient id="faintTone" cx=".5" cy=".5" r=".6">
          <stop offset="0" stop-color="#7fc6ec"/>
          <stop offset="1" stop-color="#5bbcf2"/>
        </radialGradient>
      </defs>
      <rect class="blue-field" width="1137" height="444" fill="var(--sky)"/>
      <g role="img" aria-label="Faint blue-tinted photo of a baby lying on a soft blanket">
        <rect x="700" y="0" width="437" height="444" fill="url(#faintTone)"/>
      </g>
      <rect class="window-ghost" x="566" y="146" width="400" height="212" rx="22" fill="rgba(255,255,255,.18)"/>
      <path class="corner-card" d="M890 0 H1137 V310 C1110 170 1010 60 890 0 Z" fill="var(--card)"/>
      <path d="M890 0 C1010 60 1110 170 1137 310" fill="none" stroke="var(--lime)" stroke-width="8"/>
      <g role="img" aria-label="Photo of a smiling baby in a white vest hugged close by its mother">
        <path d="M0 0 H395 C480 60 540 250 530 444 H0 Z" fill="url(#photoTone)"/>
        <path d="M0 0 H395 C480 60 540 250 530 444 H0 Z" fill="url(#photoGlow)"/>
        <path d="M0 0 H395 C480 60 540 250 530 444 H0 Z" fill="url(#photoLower)"/>
      </g>
      <path d="M395 0 C480 60 540 250 530 444" fill="none" stroke="var(--lime)" stroke-width="8"/>
    </svg>

    <div class="logo-panel">
      <div class="wordmark">Marlowe Tots</div>
      <div class="logo-descriptor">Baby Wipes</div>
    </div>

    <div class="open-tab"><span>OPEN HERE</span></div>

    <div class="mini-brand">
      <div class="wordmark-small">Marlowe Tots</div>
      <div class="line-a">Baby Wipes</div>
      <div class="line-b">Natural Baby Wipes</div>
    </div>

    <div class="count-block">
      <div class="count-badge">25</div>
      <div class="count-text">
        <div class="claim">Extra thick &amp; Soft</div>
        <div class="size">18 cm x 15.8 cm</div>
      </div>
    </div>

    <div class="fibre-claim">
      <div class="with">with</div>
      <div class="natural">natural</div>
      <div class="fibres">fibres</div>
    </div>

    <div class="proof-badge">
      <div class="big">Clinically</div>
      <div class="pill">Safe for newborn skin</div>
      <div class="big">Proven</div>
    </div>
  </section>
</body>
</html>
```